Luxury Business Card Design for High-End Window Treatments

Gilded Vantages
Custom Plantation Shutters & Architectural Shading Systems

⸻

BACK

Daniel Forsythe
Owner

Custom Interior & Exterior Window Treatments

919-482-7034
gildedvantages.com

I have included a picture that I’m hoping we can use on the back, but I’m also wondering if you can get rid of the ladder? Should we get rid of shutters , shades and blinds underneath Gilded Vantages?

Target Market(s)

High-end residential homeowners, custom home builders, architects, interior designers, and luxury renovation clients seeking premium plantation shutters and motorized architectural shading systems.

Industry/Entity Type

Custom Window treatments

Contact Information for Business Card

Front Gilded Vantages Custom Plantation Shutters Motorized Architectural Shading Systems BACK Daniel Forsythe Owner 919-482-7034 GildedVantages.com Custom Interior & Exterior Window Treatments By Appointment

Requirements
Nice to have
• Not 100% sure on nice to halves or the color but you can definitely check out my website to get a better understanding of what I’m trying to do

```html
<!DOCTYPE html>
<html lang="en">
<head>
<meta charset="utf-8">
<title>Gilded Vantages — Business Card</title>
<link href="https://fonts.googleapis.com/css2?family=Gelasio:wght@400;600&display=swap" rel="stylesheet">
<style>
  :root {
    --backdrop: #5c5c5f;
    --card: #1e1e1f;
    --gold: #f3d66b;
    --band: #fde56e;
    --ivory: #ebe7df;
    --emboss: #0d0d0e;
    --ink: #1a1a1a;
  }
  * { margin: 0; padding: 0; box-sizing: border-box; }
  html, body { width: 900px; height: 1200px; overflow: hidden; }
  body {
    background: var(--backdrop);
    font-family: "Gelasio", Georgia, serif;
    position: relative;
  }
  .card {
    position: absolute;
    left: 135px;
    width: 630px;
    height: 358px;
    background: var(--card);
    box-shadow: 0 8px 18px rgba(0,0,0,0.35);
  }
  .card--front { top: 214px; }
  .card--back { top: 628px; }

  .brand {
    position: absolute;
    left: 0; right: 0;
    text-align: center;
    font-weight: 400;
    line-height: 1;
  }
  .card--front .brand { top: 114px; font-size: 52px; color: var(--emboss); }
  .card--back .brand { top: 62px; font-size: 40px; color: var(--ivory); }
  .brand span { display: block; }
  .card--front .brand span + span { margin-top: 20px; }
  .card--back .brand span + span { margin-top: 8px; }

  .services {
    position: absolute;
    left: 0; right: 0;
    text-align: center;
    color: var(--gold);
    word-spacing: 0.6em;
    line-height: 1.2;
  }
  .card--front .services { top: 253px; font-size: 24px; }
  .card--back .services { top: 161px; font-size: 17px; }

  .person {
    position: absolute;
    right: 332px;
    top: 208px;
    text-align: right;
  }
  .person__name { font-size: 30px; color: var(--gold); line-height: 1.1; white-space: nowrap; }
  .person__role { font-size: 18px; color: var(--ivory); letter-spacing: 1px; line-height: 1.2; }

  .divider {
    position: absolute;
    left: 314px;
    top: 210px;
    width: 2px;
    height: 58px;
    background: var(--ivory);
  }

  .contact {
    position: absolute;
    left: 332px;
    top: 213px;
    list-style: none;
    color: var(--ivory);
  }
  .contact li { display: flex; align-items: center; height: 28px; white-space: nowrap; }
  .contact svg { width: 14px; height: 14px; margin-right: 10px; fill: var(--gold); flex: none; }
  .contact__phone { font-size: 18px; letter-spacing: 4px; }
  .contact__web { font-size: 18px; }

  .appointment {
    position: absolute;
    left: 0; right: 0;
    top: 305px;
    height: 29px;
    background: var(--band);
    color: var(--ink);
    font-size: 15.5px;
    font-weight: 600;
    text-align: center;
    line-height: 29px;
  }
</style>
</head>
<body>
  <section class="card card--front">
    <h1 class="brand"><span>Gilded</span><span>Vantages</span></h1>
    <p class="services">Shutters Shades Blinds</p>
  </section>

  <section class="card card--back">
    <h2 class="brand"><span>Gilded</span><span>Vantages</span></h2>
    <p class="services">Shutters Shades Blinds</p>

    <div class="person">
      <p class="person__name">Daniel Forsythe</p>
      <p class="person__role">Owner</p>
    </div>

    <div class="divider"></div>

    <ul class="contact">
      <li class="contact__phone">
        <svg viewBox="0 0 24 24" aria-hidden="true"><path d="M6.6 10.8a15.1 15.1 0 0 0 6.6 6.6l2.2-2.2c.3-.3.7-.4 1-.2 1.1.4 2.3.6 3.6.6.6 0 1 .4 1 1V20c0 .6-.4 1-1 1A17 17 0 0 1 3 4c0-.6.4-1 1-1h3.5c.6 0 1 .4 1 1 0 1.3.2 2.5.6 3.6.1.3 0 .7-.2 1l-2.3 2.2z"/></svg>
        919-482-7034
      </li>
      <li class="contact__web">
        <svg viewBox="0 0 24 24" aria-hidden="true"><path d="M12 2a10 10 0 1 0 0 20 10 10 0 0 0 0-20zm6.9 6h-2.9a15.7 15.7 0 0 0-1.4-3.6A8 8 0 0 1 18.9 8zM12 4c.8 1.2 1.5 2.5 1.9 4h-3.8c.4-1.4 1.1-2.8 1.9-4zM4.3 14a8.2 8.2 0 0 1 0-4h3.4a16.5 16.5 0 0 0 0 4H4.3zm.8 2h3c.3 1.3.8 2.5 1.4 3.6A8 8 0 0 1 5.1 16zm3-8h-3a8 8 0 0 1 4.3-3.6C8.9 5.5 8.4 6.7 8.1 8zM12 20c-.8-1.2-1.5-2.5-1.9-4h3.8c-.4 1.4-1.1 2.8-1.9 4zm2.3-6H9.7a14.7 14.7 0 0 1 0-4h4.6a14.7 14.7 0 0 1 0 4zm.3 5.6c.6-1.1 1.1-2.3 1.4-3.6h2.9a8 8 0 0 1-4.3 3.6zm1.7-5.6a16.5 16.5 0 0 0 0-4h3.4a8.2 8.2 0 0 1 0 4h-3.4z"/></svg>
        gildedvantages.com
      </li>
    </ul>

    <p class="appointment">Custom Interior &amp; Exterior Window Treatments By Appointment</p>
  </section>
</body>
</html>
```